Mirabo & Orvan Automotive Repair Shop. Need a new website design.

We specialize in Mirabo & Orvan auto repair, but also work on other Asian import vehicles. We have been in business for 7 years and pride ourselves on high quality auto repair that is fixed right the first time. Would like the automotive repair website to incorporate the colors black, red and white if possible and have our logo and some Mirabo and Orvan vehicles included in the website.

Target Market(s)

Mirabo & Orvan vehicle owners

Industry/Entity Type

Automotive Repair

Coding

Coded - Design and coding required

Number of Pages Required

5+ page

Colors
EB3D1F
EC4F4E
F09395
F8D3D4
FCEDEE

Requirements
Must have
• Home, Services, Contact Us, Schedule appointment, and a gallery tab that I can add shop pictures to when completed.
Nice to have
• Would like to see example pictures of job next to each service listed.
Should not have
• Service not related to auto repair. Ex. auto detailing, towing, car wash

```html
<!DOCTYPE html>
<html lang="en">
<head>
<meta charset="utf-8">
<title>Corvid Automotive</title>
<link href="https://fonts.googleapis.com/css2?family=Oswald:wght@500;600;700&family=Montserrat:ital,wght@0,400;0,500;0,600;0,700;1,400;1,500&display=swap" rel="stylesheet">
<style>
:root{
  --red:#eb3d1f;
  --red-2:#ec4f4e;
  --black:#0d0d0d;
  --card:#1c1c1c;
  --white:#ffffff;
  --muted:#cfcfcf;
  --head:"Oswald",sans-serif;
  --body:"Montserrat",sans-serif;
}
*{margin:0;padding:0;box-sizing:border-box}
html,body{width:1200px;height:4890px;overflow:hidden;background:var(--black);color:var(--white);font-family:var(--body)}
.page{position:relative;width:1200px;height:4890px;overflow:hidden}
section,header,footer{position:absolute;left:0;width:1200px}
.abs{position:absolute}
.btn{position:absolute;display:flex;align-items:center;justify-content:center;background:var(--red);color:#fff;font:600 13px var(--body);text-transform:uppercase;letter-spacing:.3px}
.btn.ghost{background:transparent;border:1.5px solid #fff}
.btn.outline{background:transparent;border:1.5px solid var(--red);color:var(--red)}
.eyebrow{position:absolute;color:var(--red);font:500 17px var(--body);text-transform:uppercase}
.h2{position:absolute;font:600 50px/1 var(--head);text-transform:uppercase;letter-spacing:.5px}
.texture{background:radial-gradient(circle at 50% 50%,#1d1d1d 0 1.5px,transparent 2px) 0 0/7px 7px,#111}

/* header / hero */
.hero{top:0;height:625px;background:radial-gradient(ellipse at 70% 45%,#3a3a3a 0,#1c1c1c 45%,#0b0b0b 100%)}
.hero-photo{position:absolute;left:480px;top:150px;width:720px;height:400px;background:linear-gradient(90deg,rgba(40,40,40,0) 0,rgba(120,24,28,.45) 35%,rgba(140,28,32,.55) 70%,rgba(40,40,40,.3) 100%)}
.brand{position:absolute;left:100px;top:36px;display:flex;align-items:center;gap:10px;font:700 22px var(--body);color:#fff}
.brand-mark{width:16px;height:16px;background:var(--red)}
.nav{position:absolute;left:394px;top:36px;display:flex;gap:48px;font:500 14px var(--body);text-transform:uppercase}
.nav .active{color:var(--red);font-style:italic;border-bottom:2px solid var(--red);padding-bottom:6px}
.talk{left:968px;top:27px;width:130px;height:40px;background:transparent;border:1.5px solid var(--red)}
.hero h1{position:absolute;left:100px;top:232px;font:600 40px/44px var(--head);text-transform:uppercase}
.hero .tag{position:absolute;left:100px;top:340px;font:500 17px var(--head)}

/* about */
.about{top:625px;height:650px}
.about-img1{left:100px;top:88px;width:373px;height:367px;background:linear-gradient(160deg,#4b5546,#1f2420 60%,#6b4a1e)}
.about-img2{left:233px;top:273px;width:359px;height:344px;background:linear-gradient(140deg,#7d8ea5,#2d3b52 55%,#111);border:2px solid #fff}
.about-frame{left:145px;top:138px;width:372px;height:410px;border:2px solid var(--red)}
.play{left:505px;top:530px;width:48px;height:48px}
.about .rule{position:absolute;left:657px;top:150px;width:82px;height:2px;background:var(--red)}
.about-copy{position:absolute;left:657px;top:245px;width:443px;font:400 15px/31.5px var(--body);color:var(--muted);text-align:justify}

/* services */
.services{top:1275px;height:765px}
.services .sub{position:absolute;left:300px;top:154px;width:600px;text-align:center;font:400 13px/23px var(--body)}
.svc{position:absolute;top:235px;width:237px;height:365px;background:var(--card)}
.svc .ph{height:163px}
.svc .badge{position:absolute;left:95px;top:135px;width:48px;height:54px;background:var(--red);border:3px solid #fff;border-radius:4px 4px 24px 24px}
.svc h3{position:absolute;top:215px;width:100%;text-align:center;font:600 18px var(--body)}
.svc p{position:absolute;top:250px;left:14px;right:14px;text-align:center;font:400 13px/25px var(--body);color:var(--muted)}
.svc .arr{position:absolute;top:335px;left:106px}
.chev{position:absolute;top:405px}

/* banner */
.banner{top:2040px;height:510px;background:#141414}
.banner-photo{left:560px;top:0;width:640px;height:510px;background:linear-gradient(110deg,#1a1a1a 0,#5a1e16 40%,#d9884a 100%)}
.banner h2{position:absolute;left:100px;top:100px;font:700 italic 54px/60px var(--head)}
.banner .hub{position:absolute;left:100px;top:220px;font:400 50px/60px var(--body)}
.banner .hub span{color:var(--red)}

/* blog */
.blog{top:2550px;height:735px}
.post{position:absolute;top:190px;width:313px;height:470px;background:var(--card)}
.post .ph{height:210px}
.post .date{position:absolute;right:16px;top:180px;width:40px;height:50px;background:var(--red);text-align:center;font:700 22px/26px var(--head)}
.post .date small{display:block;font:500 11px/14px var(--body)}
.post .meta{position:absolute;left:16px;top:235px;font:500 12px var(--body);color:var(--red)}
.post h3{position:absolute;left:16px;top:265px;font:600 18px var(--body)}
.post p{position:absolute;left:16px;right:16px;top:305px;font:400 13px/27px var(--body);color:var(--muted)}
.post .btn{left:16px;top:415px;width:140px;height:36px;font-size:12px}

/* testimonials */
.reviews{top:3285px;height:483px;background:linear-gradient(90deg,#1a1a1a,#0f0f0f 60%,#2a0c0b)}
.reviews-photo{left:0;top:0;width:620px;height:483px;background:linear-gradient(120deg,#5a5a5a,#262626 45%,#7a1a14 80%,#1a1a1a)}
.reviews .rule{position:absolute;left:655px;top:110px;width:82px;height:2px;background:var(--red)}
.quote{position:absolute;left:657px;width:450px;font:italic 400 15px/28px var(--body)}
.who{position:absolute;left:657px;font:500 18px var(--body)}

/* contact */
.contact{top:3768px;height:500px;background:linear-gradient(90deg,#3c3c3a,#3a3a3c 50%,#4a4d51)}
.contact-photo{left:580px;top:0;width:620px;height:500px;background:linear-gradient(100deg,rgba(58,58,60,0) 0,#2a2c30 35%,#1d1e21 70%,#3a2e28 100%)}
.contact .rule{position:absolute;left:100px;top:82px;width:82px;height:2px;background:var(--red)}
.contact p{position:absolute;left:100px;top:225px;width:460px;font:400 15px/32px var(--body)}

/* newsletter */
.newsletter{top:4268px;height:292px;background:#1a1a1a}
.newsletter h2{position:absolute;width:100%;top:60px;text-align:center;font:600 40px var(--head);text-transform:uppercase}
.field-label{position:absolute;top:140px;font:500 12px var(--body);text-transform:uppercase}
.field{position:absolute;top:165px;width:300px;height:40px;background:#fff;color:#333;font:400 13px var(--body);padding:12px}

/* footer */
.footer{top:4560px;height:330px;background:#121212}
.foot-brand{position:absolute;left:100px;top:100px;display:flex;align-items:center;gap:12px;font:700 30px var(--body)}
.foot-brand i{width:22px;height:22px;background:var(--red)}
.col{position:absolute;top:62px}
.col h4{font:600 16px var(--head);text-transform:uppercase;margin-bottom:12px}
.col li{list-style:none;font:400 15px/32px var(--body)}
.info li{display:flex;gap:8px;font:400 14px/22px var(--body);margin-bottom:10px;width:290px}
.info svg{flex:none;margin-top:3px}
.copy{position:absolute;left:100px;top:285px;font:400 14px var(--body)}
.social{position:absolute;top:266px;width:38px;height:38px;border-radius:50%;background:var(--red)}
</style>
</head>
<body>
<div class="page">

<header class="hero">
  <div class="hero-photo" role="img" aria-label="Red Mirabo sedan in a dark studio"></div>
  <div class="brand"><span class="brand-mark"></span>CORVID</div>
  <nav class="nav"><span class="active">Home</span><span>About Us</span><span>Services</span><span>Blog</span><span>Contact Us</span></nav>
  <a class="btn talk">Let's Talk</a>
  <h1>Dealership Quality at<br>Affordable Prices</h1>
  <div class="tag">Specializing in Mirabo, Orvan, &amp; Velto Auto Repair</div>
  <a class="btn" style="left:100px;top:397px;width:270px;height:38px">Schedule an Appointment</a>
</header>

<section class="about texture">
  <div class="abs about-frame"></div>
  <div class="abs about-img1" role="img" aria-label="Mirabo pickup truck with headlights on at dusk"></div>
  <div class="abs about-img2" role="img" aria-label="Mechanic working on an engine bay"></div>
  <svg class="abs play" viewBox="0 0 48 48"><circle cx="24" cy="24" r="22" fill="#111" stroke="#fff" stroke-width="2"/><path d="M19 15l14 9-14 9z" fill="#fff"/></svg>
  <div class="rule"></div>
  <div class="eyebrow" style="left:757px;top:139px">About Us</div>
  <div class="h2" style="left:657px;top:175px">Corvid Automotive</div>
  <p class="about-copy">Here at Corvid Automotive, we believe in professional service and high quality auto repairs. With over 20 years of Mirabo, Orvan, &amp; Velto dealership experience, we have all the tools, equipment, and knowledge to keep your Mirabo, Orvan, &amp; Velto vehicle running strong. Although we specialize in these makes, we also repair &amp; service other import makes like Hanaro, Aceva, Nivara, Infora, Keto, Hyolan, Mizuko, etc.</p>
  <a class="btn" style="left:657px;top:525px;width:158px;height:38px">Learn More</a>
</section>

<section class="services texture">
  <div class="eyebrow" style="left:0;width:1200px;text-align:center;top:57px">Our Services</div>
  <div class="h2" style="left:0;width:1200px;text-align:center;top:93px">What We Offer</div>
  <p class="sub">Don't see the service you think you need? Contact us anyway! This list is not comprehensive of everything we're capable of!</p>
  <svg class="chev" style="left:62px" width="14" height="26" viewBox="0 0 14 26"><path d="M12 2L2 13l10 11" fill="none" stroke="#aaa" stroke-width="2"/></svg>
  <svg class="chev" style="left:1122px" width="14" height="26" viewBox="0 0 14 26"><path d="M2 2l10 11L2 24" fill="none" stroke="#aaa" stroke-width="2"/></svg>

  <div class="svc" style="left:100px"><div class="ph" role="img" aria-label="Engine being lifted in a workshop" style="background:linear-gradient(150deg,#9aa4ad,#3a3f45)"></div><div class="badge"></div><h3>Engine Replacement</h3><p>Lorem ipsmet,etur adipiscing elit, ssmod tempor incididunt ut labore et dolore</p><svg class="arr" width="26" height="12" viewBox="0 0 26 12"><path d="M0 6h24M19 1l5 5-5 5" fill="none" stroke="#fff" stroke-width="1.6"/></svg></div>
  <div class="svc" style="left:355px"><div class="ph" role="img" aria-label="Technician servicing a brake disc" style="background:linear-gradient(150deg,#5a6a7a,#26262a)"></div><div class="badge"></div><h3>Brakes</h3><p>Lorem ipsmet,etur adipiscing elit, ssmod tempor incididunt ut labore et dolore</p><svg class="arr" width="26" height="12" viewBox="0 0 26 12"><path d="M0 6h24M19 1l5 5-5 5" fill="none" stroke="#fff" stroke-width="1.6"/></svg></div>
  <div class="svc" style="left:608px"><div class="ph" role="img" aria-label="Close-up of engine cylinder components" style="background:linear-gradient(150deg,#b0b0b0,#3c3c3c)"></div><div class="badge"></div><h3>Front Engine Seals</h3><p>Lorem ipsmet,etur adipiscing elit, ssmod tempor incididunt ut labore et dolore</p><svg class="arr" width="26" height="12" viewBox="0 0 26 12"><path d="M0 6h24M19 1l5 5-5 5" fill="none" stroke="#fff" stroke-width="1.6"/></svg></div>
  <div class="svc" style="left:863px"><div class="ph" role="img" aria-label="Wheel alignment equipment on a tire" style="background:linear-gradient(150deg,#d0d2d4,#4a4a4a)"></div><div class="badge"></div><h3>Alignments</h3><p>Lorem ipsmet,etur adipiscing elit, ssmod tempor incididunt ut labore et dolore</p><svg class="arr" width="26" height="12" viewBox="0 0 26 12"><path d="M0 6h24M19 1l5 5-5 5" fill="none" stroke="#fff" stroke-width="1.6"/></svg></div>

  <a class="btn" style="left:522px;top:633px;width:156px;height:38px">View More</a>
</section>

<section class="banner">
  <div class="abs banner-photo" role="img" aria-label="Technician polishing a car under red lights"></div>
  <h2>Texas Largest Car<br>Care Facility</h2>
  <div class="hub"><span>Automotive</span> Hub<br>for Enthusiasts</div>
  <a class="btn" style="left:100px;top:366px;width:156px;height:38px">Learn More</a>
  <a class="btn ghost" style="left:270px;top:366px;width:156px;height:38px">Contact Us</a>
</section>

<section class="blog texture">
  <div class="eyebrow" style="left:0;width:1200px;text-align:center;top:70px">Resources</div>
  <div class="h2" style="left:0;width:1200px;text-align:center;top:105px">Latest News &amp; Blogs</div>

  <article class="post" style="left:100px"><div class="ph" role="img" aria-label="Timing gear and engine parts" style="background:linear-gradient(150deg,#8a8e90,#2a2c2e)"></div><div class="date">01<small>FEB</small></div><div class="meta">23 Comments &nbsp;|&nbsp; by John Doe</div><h3>Finibus Bonorum et Malorum</h3><p>Lorem ipsum dolor sit amet, consectetur adipiscing elit, sepor incididunt ut labore et dolore magna alis ipsum suspendisse ultrices gravida.</p><a class="btn outline">More Info</a></article>
  <article class="post" style="left:444px"><div class="ph" role="img" aria-label="Gloved hands working on an engine" style="background:linear-gradient(150deg,#9bb0c4,#2a3442)"></div><div class="date">01<small>FEB</small></div><div class="meta">23 Comments &nbsp;|&nbsp; by John Doe</div><h3>Finibus Bonorum et Malorum</h3><p>Lorem ipsum dolor sit amet, consectetur adipiscing elit, sepor incididunt ut labore et dolore magna alis ipsum suspendisse ultrices gravida.</p><a class="btn outline">More Info</a></article>
  <article class="post" style="left:787px"><div class="ph" role="img" aria-label="Service advisor talking with customers in a shop" style="background:linear-gradient(150deg,#a8b2ba,#3e3a36)"></div><div class="date">01<small>FEB</small></div><div class="meta">23 Comments &nbsp;|&nbsp; by John Doe</div><h3>Finibus Bonorum et Malorum</h3><p>Lorem ipsum dolor sit amet, consectetur adipiscing elit, sepor incididunt ut labore et dolore magna alis ipsum suspendisse ultrices gravida.</p><a class="btn outline">More Info</a></article>
</section>

<section class="reviews">
  <div class="abs reviews-photo" role="img" aria-label="Detailer buffing a car in a dim garage"></div>
  <div class="rule"></div>
  <div class="eyebrow" style="left:743px;top:99px">Reviews</div>
  <div class="h2" style="left:655px;top:135px">Testimonials</div>
  <p class="quote" style="top:200px">I would highly recommend Corvid Automotive to family, friends, &amp; co-workers! I'm a repeat customer myself!</p>
  <div class="who" style="top:268px">-Daniel R.</div>
  <p class="quote" style="top:300px">Corvid Automotive is my go to car repair company. I trust them with all my vehicle needs.</p>
  <div class="who" style="top:365px">-Marisa T.</div>
</section>

<section class="contact">
  <div class="abs contact-photo" role="img" aria-label="Dark grey Orvan sedan parked at dusk"></div>
  <div class="rule"></div>
  <div class="eyebrow" style="left:188px;top:71px">Let's Talk</div>
  <div class="h2" style="left:100px;top:130px">Get in Touch</div>
  <p>Sed ut perspiciatis undnis iste natus error sit voluptatem accusantium dolorque laudantium, totam rem aperiam, eaque ipsa quae ab illo inventore veritatis</p>
  <a class="btn" style="left:100px;top:337px;width:156px;height:38px">Contact Us</a>
</section>

<section class="newsletter">
  <h2>Sign Up to the Newsletter Today</h2>
  <div class="field-label" style="left:198px">Name</div>
  <div class="field" style="left:198px">John Doe</div>
  <div class="field-label" style="left:514px">Email Address</div>
  <div class="field" style="left:514px">John Doe</div>
  <a class="btn" style="left:828px;top:165px;width:174px;height:40px">Subscribe</a>
</section>

<footer class="footer">
  <div class="foot-brand"><i></i>CORVID</div>
  <div class="col" style="left:393px"><h4>Quick Links</h4><ul><li>Home</li><li>About Us</li><li>Services</li><li>Blog</li><li>Contact Us</li></ul></div>
  <div class="col" style="left:573px"><h4>Other Links</h4><ul><li>About Us</li><li>Terms &amp; Conditions</li><li>FAQs</li><li>Gallery</li></ul></div>
  <div class="col info" style="left:812px"><h4>Contact Info</h4><ul>
    <li><svg width="14" height="16" viewBox="0 0 14 16"><path d="M7 1a5 5 0 0 1 5 5c0 4-5 9-5 9S2 10 2 6a5 5 0 0 1 5-5z" fill="var(--red)"/><circle cx="7" cy="6" r="2" fill="#121212"/></svg>418 Harbor Ridge Dr Suite 2, Fairmont, TX 75000, United States</li>
    <li><svg width="14" height="14" viewBox="0 0 14 14"><path d="M3 1l3 3-2 2a8 8 0 0 0 4 4l2-2 3 3-2 2C6 13 1 8 1 3z" fill="var(--red)"/></svg>555.014.2287</li>
    <li><svg width="14" height="12" viewBox="0 0 14 12"><rect x="0" y="1" width="14" height="10" fill="var(--red)"/><path d="M0 1l7 5 7-5" fill="none" stroke="#121212"/></svg>CorvidAutomotiveLLC@example.com</li>
    <li><svg width="14" height="12" viewBox="0 0 14 12"><rect x="0" y="1" width="14" height="10" fill="var(--red)"/><path d="M0 1l7 5 7-5" fill="none" stroke="#121212"/></svg>Hours of Operation M-F &nbsp;8:30-6pm</li>
  </ul></div>
  <div class="copy">©Copyright 2024 Corvid Automotive. All Rights Reserved.</div>
  <div class="social" style="left:902px"></div>
  <div class="social" style="left:954px"></div>
  <div class="social" style="left:1008px"></div>
  <div class="social" style="left:1060px"></div>
</footer>

</div>
</body>
</html>
```